Wealth Management Business Card

We are a professional services consulting firm that specializes in high net worth individuals over $25,000,000, executives C-suite and above, closely held businesses owners, family offices and highly compensated employees.

Our focus is on risk mitigation and tax efficient strategies. Our clients take their risk on themselves and have a proven track record generating wealth. Our directive is to preserve and protect the wealth they’ve already created.

Our company Harrowgate Advisory is geared around five directives of asset protection:
1) Legal Structuring
2) Leverage & Financing
3) Risk Management - Asset Protection & Insurance, Trustee Work
4) Asset Management & Investing - Under www.qlvbrookfield.com
5) Tax Efficient Strategies

Our Company Mark is a Pentagon with a key in the middle. A pentagon is the most efficient defensive structure. Each point of a pentagon is equal distance front every point . Each side provides support to another and works together, which is the key to our clients success.

Our key colors are blue, black and silver.

We ‘re located in the Pacific Northwest with bi coastal and international clients. We have fewer, higher net worth clients and provide exceptional customer service. We do not do social media.

website is www.harrowgatepath.com

Target Market(s)

High End Clients

Contact Information for Business Card

extra thick

Font styles to use
Serif

Requirements
Must have
• Metalic foil for lettering.
Black Background on one side
White Background on the other
Horizontal Format Only
No Rounded corners
Not Marketing sales information on the card.
Nice to have
• imprinted texture on the card
Should not have
• lots of color

```html
<!DOCTYPE html>
<html lang="en">
<head>
<meta charset="utf-8">
<title>Harrowgate Advisory — Business Card</title>
<link href="https://fonts.googleapis.com/css2?family=Cinzel:wght@500&family=Poppins:wght@400;600&display=swap" rel="stylesheet">
<style>
  :root{
    --stage:#d9dadc;
    --card-white:#ffffff;
    --card-black:#262627;
    --navy:#1b2a78;
    --accent-blue:#1d7fd1;
    --ink-grey:#555a60;
    --silver:#e4e6e8;
    --emboss-light:#2f2f31;
    --emboss-dark:#161617;
    --rule:#2c3f8f;
  }
  *{margin:0;padding:0;box-sizing:border-box}
  html,body{width:1200px;height:856px;overflow:hidden}
  body{
    background:var(--stage);
    font-family:"Poppins",sans-serif;
    position:relative;
  }
  .card{
    position:absolute;
    left:290px;
    width:620px;height:354px;
    box-shadow:0 10px 28px rgba(0,0,0,.22);
    overflow:hidden;
  }
  .card--front{top:50px;background:var(--card-white)}
  .card--back{top:452px;background:var(--card-black)}

  /* front */
  .brand{
    position:absolute;left:30px;top:0;width:270px;height:100%;
    display:flex;flex-direction:column;align-items:center;justify-content:center;gap:20px;
  }
  .brand__mark{width:40px;height:40px;background:var(--navy)}
  .brand__name{
    font-family:"Cinzel",serif;font-weight:500;font-size:30px;line-height:1.1;
    color:var(--navy);text-align:center;letter-spacing:1px;
  }
  .divider{
    position:absolute;left:318px;top:62px;width:1.5px;height:230px;background:var(--rule);
  }
  .contact{
    position:absolute;left:346px;top:66px;width:250px;color:var(--ink-grey);
  }
  .contact__name{font-weight:600;font-size:21px;color:var(--navy);line-height:1.2}
  .contact__role{font-size:14px;margin-bottom:16px}
  .contact__address{font-size:14px;line-height:1.45;margin-bottom:14px}
  .contact__list{list-style:none;font-size:14px;line-height:1.55}
  .contact__list li{display:flex;align-items:center;gap:7px}
  .contact__list svg{width:12px;height:12px;flex:none;fill:var(--accent-blue)}

  /* back */
  .emblem-area{
    position:absolute;left:40px;top:30px;width:260px;height:260px;
    background:linear-gradient(135deg,var(--emboss-light),var(--emboss-dark));
    box-shadow:inset 2px 2px 3px rgba(255,255,255,.05),inset -3px -3px 6px rgba(0,0,0,.35);
  }
  .back-brand{
    position:absolute;left:330px;right:30px;bottom:60px;
    display:flex;flex-direction:column;align-items:center;gap:10px;
  }
  .back-brand__rule{width:220px;height:1px;background:var(--silver);opacity:.7}
  .back-brand__name{
    font-family:"Cinzel",serif;font-weight:500;font-size:32px;line-height:1.1;
    color:var(--silver);letter-spacing:1px;text-align:center;
  }
</style>
</head>
<body>

<section class="card card--front" aria-label="Card front">
  <div class="brand">
    <div class="brand__mark"></div>
    <div class="brand__name">Harrowgate<br>Advisory</div>
  </div>
  <div class="divider"></div>
  <div class="contact">
    <p class="contact__name">Corwin Aldersley</p>
    <p class="contact__role">Founder</p>
    <p class="contact__address">418 W Birch Ave, Suite 112<br>Maple Ridge, OR 97120</p>
    <ul class="contact__list">
      <li>
        <svg viewBox="0 0 24 24" aria-hidden="true"><path d="M6.6 10.8a15 15 0 0 0 6.6 6.6l2.2-2.2c.3-.3.7-.4 1-.2 1.1.4 2.3.6 3.6.6.6 0 1 .4 1 1V20c0 .6-.4 1-1 1A17 17 0 0 1 3 4c0-.6.4-1 1-1h3.5c.6 0 1 .4 1 1 0 1.3.2 2.5.6 3.6.1.3 0 .7-.2 1z"/></svg>
        (503) 555-0147
      </li>
      <li>
        <svg viewBox="0 0 24 24" aria-hidden="true"><path d="M2 5h20v14H2zM3.5 6.5v.4L12 12.5l8.5-5.6v-.4z"/></svg>
        info@harrowgatepath.com
      </li>
      <li>
        <svg viewBox="0 0 24 24" aria-hidden="true"><circle cx="12" cy="12" r="10"/></svg>
        www.harrowgatepath.com
      </li>
    </ul>
  </div>
</section>

<section class="card card--back" aria-label="Card back">
  <div class="emblem-area" role="img" aria-label="Large embossed brand emblem area"></div>
  <div class="back-brand">
    <div class="back-brand__rule"></div>
    <div class="back-brand__name">Harrowgate<br>Advisory</div>
    <div class="back-brand__rule"></div>
  </div>
</section>

</body>
</html>
```